Need a graphic design for front page of tech blog

Hi,

So I'm looking to start a project of redesigning the front homepage for all of my tech sites. I already have a developer that will code the change, so what I need from someone here is to give me a graphic design, which I can then give to my developers to code.

Currently, I have the plain old boring default list of WordPress posts as the front page, which needs to be replaced with something a little more like a magazine or newspaper style. You can see my four sites here:

https://www.quill-gadget-notes.com/
https://servicebenchnerd.com/
https://theatticbitworks.com/
https://www.hoppingtolark.com/

I've attached some screenshots of mobile sites that I like in terms of look and style. Some desktop sites that I like are here (I like some parts more than others, I've attached screenshots of the sections I like):

https://www.ploddernook.com/
https://www.gizmonest.com/
https://www.pinewirebulletin.com/
https://www.takeholdwith.com/
https://www.dayspool.com/

Basically, I don't need all that text after each post. Seems like most sites now just have an image, a title, the author and date info and possibly the category.

Right now I'm only showing 10 posts and one has to scroll through lots of text to see them all. The sidebar is good, but I think we can get rid of that for the front page and instead have different sections like Latest Tips, and then some section headers based on the categories.

Anyway, I'm looking for someone who can come up with multiple designs, so that I have some choice.

I'm looking to get this done over the next few weeks. Also, please include in your price the cost of any revisions and how many revisions can be done.

Thanks

Tarun

```html
<!DOCTYPE html>
<html lang="en">
<head>
<meta charset="utf-8">
<title>Quill Gadget Notes — Home</title>
<link rel="stylesheet" href="https://fonts.googleapis.com/css2?family=Montserrat:wght@400;500;600;700&family=Roboto:wght@300;400;500&display=swap">
<style>
:root{
  --orange:#f47a30;
  --orange-dark:#e8601c;
  --ink:#111111;
  --text:#444444;
  --muted:#777777;
  --line:#d5d5d5;
  --soft-bg:#f1f1f1;
  --footer-bg:#e6e6e6;
  --white:#ffffff;
}
*{box-sizing:border-box;margin:0;padding:0}
html,body{width:1200px;height:4918px;overflow:hidden;background:var(--white)}
body{position:relative;font-family:'Roboto',sans-serif;color:var(--text)}
.abs{position:absolute}
a{color:inherit;text-decoration:none}

/* header */
.site-header{left:0;top:0;width:1200px;height:72px;background:var(--white);display:flex;align-items:center;justify-content:space-between;padding:0 112px;z-index:3}
.brand{display:flex;align-items:center;gap:8px;font-family:'Montserrat',sans-serif;font-weight:700;font-size:17px;letter-spacing:.5px;color:var(--ink);text-transform:uppercase}
.brand-dot{width:12px;height:12px;border-radius:50%;background:var(--orange)}
.main-nav{display:flex;align-items:center;gap:28px;font-family:'Montserrat',sans-serif;font-size:14px;color:var(--ink)}
.main-nav .active{color:var(--orange)}
.search-icon{width:16px;height:16px}

/* hero */
.hero{left:0;top:72px;width:1200px;height:676px;overflow:hidden}
.hero-photo{position:absolute;inset:0;background:linear-gradient(135deg,#bfc2c4 0%,#d9dbdc 45%,#c4c7c9 100%)}
.hero-shade{position:absolute;inset:0;background:rgba(60,60,60,.28)}
.hero-content{position:absolute;left:0;top:210px;width:1200px;text-align:center;color:var(--white)}
.hero-title{font-family:'Montserrat',sans-serif;font-weight:700;font-size:48px;margin-bottom:18px}
.hero-lead{font-size:20px;line-height:32px;width:640px;margin:0 auto 38px;font-weight:300}
.hero-btn{display:inline-block;width:216px;height:54px;line-height:50px;border:2px solid var(--white);border-radius:27px;font-family:'Montserrat',sans-serif;font-weight:600;font-size:15px;letter-spacing:.5px}
.hero-swoosh{position:absolute;left:0;bottom:0;width:1200px;height:110px}
.hero-dots{position:absolute;left:0;top:624px;width:1200px;display:flex;justify-content:center;gap:10px}
.hero-dots span{width:10px;height:10px;border-radius:50%;background:rgba(255,255,255,.8)}
.hero-dots span:first-child{background:var(--orange)}

/* tabs */
.category-tabs{left:112px;top:876px;width:976px;height:50px;border-bottom:2px solid var(--line);display:flex}
.category-tabs a{font-family:'Montserrat',sans-serif;font-size:20px;color:var(--ink);padding:0 12px;height:48px;line-height:46px;margin-right:64px;letter-spacing:.5px}
.category-tabs a.active{color:var(--orange);border-bottom:2px solid var(--orange);margin-bottom:-2px;height:50px}

/* posts */
.post{left:112px;width:976px}
.post-image{width:976px;height:386px}
.post-title{font-family:'Montserrat',sans-serif;font-weight:600;font-size:38px;line-height:50px;color:var(--ink);margin-top:42px;width:720px}
.post-meta{display:flex;align-items:center;gap:10px;margin-top:22px;font-size:14px;color:var(--text)}
.post-meta svg{width:17px;height:17px}
.meta-sep{margin:0 14px;color:var(--muted)}
.post-excerpt{margin-top:22px;font-size:17px;line-height:32px;color:var(--text);width:976px}
.btn-read{display:inline-block;margin-top:24px;width:316px;height:64px;line-height:64px;text-align:center;background:var(--orange);color:var(--white);border-radius:32px;font-family:'Montserrat',sans-serif;font-weight:600;font-size:16px;letter-spacing:.5px}

/* blog */
.blog-section{left:0;top:3595px;width:1200px;height:722px;background:var(--soft-bg)}
.section-title{font-family:'Montserrat',sans-serif;font-weight:600;font-size:40px;color:var(--ink);text-align:center;letter-spacing:1px}
.blog-section .section-title{position:absolute;top:80px;width:1200px}
.blog-grid{position:absolute;left:112px;top:184px;display:flex;gap:33px}
.blog-card{width:303px}
.card-image{width:303px;height:190px}
.card-head{display:flex;gap:14px;margin-top:18px}
.date-badge{flex:none;width:44px;height:44px;border-radius:50%;background:var(--orange);color:var(--white);text-align:center;font-family:'Montserrat',sans-serif;font-weight:700;font-size:14px;line-height:14px;padding-top:9px}
.date-badge small{display:block;font-size:8px;font-weight:500;line-height:12px}
.card-title{font-family:'Montserrat',sans-serif;font-weight:600;font-size:17px;line-height:22px;color:var(--ink)}
.card-text{margin-top:12px;font-size:14px;line-height:24px;color:var(--muted)}
.btn-outline{display:inline-block;margin-top:24px;width:150px;height:42px;line-height:40px;text-align:center;border:1.5px solid var(--ink);border-radius:21px;font-family:'Montserrat',sans-serif;font-weight:500;font-size:13px;color:var(--ink)}

/* newsletter */
.newsletter{left:0;top:4317px;width:1200px;height:367px;background:var(--white);text-align:center}
.newsletter .section-title{margin-top:84px;font-size:42px}
.newsletter-text{margin:22px auto 0;width:560px;font-size:16px;line-height:28px;color:var(--text)}
.subscribe-form{display:flex;margin:38px auto 0;width:738px;height:56px}
.subscribe-input{flex:1;border:1px solid var(--line);border-right:none;font-size:15px;color:var(--text);text-align:left;padding-left:46px;line-height:54px}
.subscribe-btn{width:145px;background:var(--orange);color:var(--white);font-family:'Montserrat',sans-serif;font-weight:600;font-size:16px;line-height:56px}

/* footer */
.site-footer{left:0;top:4684px;width:1200px;height:234px;background:var(--footer-bg);text-align:center}
.site-footer .brand{justify-content:center;margin-top:50px}
.social-row{display:flex;justify-content:center;gap:8px;margin-top:22px}
.social-row span{width:30px;height:30px;border-radius:50%;border:1.5px solid var(--ink)}
.footer-nav{display:flex;justify-content:center;gap:40px;margin-top:20px;font-family:'Montserrat',sans-serif;font-weight:600;font-size:15px;color:var(--ink)}
.copyright{margin-top:16px;font-family:'Montserrat',sans-serif;font-weight:600;font-size:14px;color:var(--ink)}
</style>
</head>
<body>

<header class="site-header abs">
  <a class="brand" href="#"><span class="brand-dot"></span>Quill Gadget Notes</a>
  <nav class="main-nav">
    <a class="active" href="#">Home</a>
    <a href="#">Desktop</a>
    <a href="#">Tips</a>
    <a href="#">Software</a>
    <a href="#">Other</a>
    <svg class="search-icon" viewBox="0 0 16 16" fill="none" stroke="#f47a30" stroke-width="2"><circle cx="6.5" cy="6.5" r="5"/><line x1="10.5" y1="10.5" x2="15" y2="15"/></svg>
  </nav>
</header>

<section class="hero abs">
  <div class="hero-photo" role="img" aria-label="Top-down photo of a white desk with keyboard, notebook, coffee cup and plant"></div>
  <div class="hero-shade"></div>
  <div class="hero-content">
    <h1 class="hero-title">Quill Gadget Notes</h1>
    <p class="hero-lead">It doesn't matter if your password is 32 characters long, alphanumeric, and would take several quintillion years to crack—it's not secure</p>
    <a class="hero-btn" href="#">GET STARTED</a>
  </div>
  <svg class="hero-swoosh" viewBox="0 0 1200 110" preserveAspectRatio="none">
    <path d="M0 30 C300 70 700 80 1200 0 L1200 110 L0 110 Z" fill="#f47a30"/>
    <path d="M0 70 C350 95 750 80 1200 40 L1200 110 L0 110 Z" fill="#e8601c"/>
    <path d="M0 95 C400 100 800 90 1200 70 L1200 110 L0 110 Z" fill="#ffffff"/>
  </svg>
  <div class="hero-dots"><span></span><span></span><span></span><span></span></div>
</section>

<nav class="category-tabs abs">
  <a class="active" href="#">DESKTOP</a>
  <a href="#">TIPS</a>
  <a href="#">SOFTWARE</a>
  <a href="#">OTHER</a>
</nav>

<article class="post abs" style="top:977px">
  <div class="post-image" role="img" aria-label="Hooded figure at a laptop beside a red screen reading Data Leaked" style="background:linear-gradient(90deg,#1a1d24 0%,#3a1414 55%,#8c1c1c 100%)"></div>
  <h2 class="post-title">How to Know If Your Password Has Leaked Online</h2>
  <div class="post-meta">
    <svg viewBox="0 0 18 18" fill="none" stroke="#444" stroke-width="1.4"><circle cx="9" cy="9" r="8"/><circle cx="9" cy="7" r="3"/><path d="M3.5 14.5c1.5-2.5 9.5-2.5 11 0"/></svg>
    <span>Dorian Pellham</span><span class="meta-sep">|</span>
    <svg viewBox="0 0 18 18" fill="none" stroke="#444" stroke-width="1.4"><rect x="2" y="3" width="14" height="13"/><line x1="2" y1="7" x2="16" y2="7"/><line x1="6" y1="1" x2="6" y2="4"/><line x1="12" y1="1" x2="12" y2="4"/></svg>
    <span>February 27, 2019</span>
  </div>
  <p class="post-excerpt">It doesn't matter if your password is 32 characters long, alphanumeric, and would take several quintillion years to crack—it's not secure. As a matter of fact, anything that touches the Internet isn't secure! This is because password security does not only come at the discretion of the user who has created it but also the [...]</p>
  <a class="btn-read" href="#">CONTINUE READING</a>
</article>

<article class="post abs" style="top:1840px">
  <div class="post-image" role="img" aria-label="Flat illustration of two remote workers at desks with laptops on a light blue background" style="background:linear-gradient(180deg,#8ecfee 0%,#a9dcf3 70%,#ffffff 100%)"></div>
  <h2 class="post-title">Top 10 Collaboration Tools for Remote Teams</h2>
  <div class="post-meta">
    <svg viewBox="0 0 18 18" fill="none" stroke="#444" stroke-width="1.4"><circle cx="9" cy="9" r="8"/><circle cx="9" cy="7" r="3"/><path d="M3.5 14.5c1.5-2.5 9.5-2.5 11 0"/></svg>
    <span>Dorian Pellham</span><span class="meta-sep">|</span>
    <svg viewBox="0 0 18 18" fill="none" stroke="#444" stroke-width="1.4"><rect x="2" y="3" width="14" height="13"/><line x1="2" y1="7" x2="16" y2="7"/><line x1="6" y1="1" x2="6" y2="4"/><line x1="12" y1="1" x2="12" y2="4"/></svg>
    <span>February 26, 2019</span>
  </div>
  <p class="post-excerpt">Orbitel released Nimbus Pie to its own phones, namely the Prism brand, in August of last year. Since then, the various manufacturers of Nimbus phones, including Korvane, Velotra, Hanlou, Sorin, Nordell, Halden, KV, and others, have been adapting the latest version of Nimbus (ver. 9) to their phones.</p>
  <a class="btn-read" href="#">CONTINUE READING</a>
</article>

<article class="post abs" style="top:2696px">
  <div class="post-image" role="img" aria-label="Browser new-tab page with waterfall landscape, large clock reading 6:39 and a greeting" style="background:linear-gradient(180deg,#4d5a52 0%,#6f7d72 50%,#2e3a33 100%)"></div>
  <h2 class="post-title">The Best Beacon Extensions for Productivity</h2>
  <div class="post-meta">
    <svg viewBox="0 0 18 18" fill="none" stroke="#444" stroke-width="1.4"><circle cx="9" cy="9" r="8"/><circle cx="9" cy="7" r="3"/><path d="M3.5 14.5c1.5-2.5 9.5-2.5 11 0"/></svg>
    <span>Dorian Pellham</span><span class="meta-sep">|</span>
    <svg viewBox="0 0 18 18" fill="none" stroke="#444" stroke-width="1.4"><rect x="2" y="3" width="14" height="13"/><line x1="2" y1="7" x2="16" y2="7"/><line x1="6" y1="1" x2="6" y2="4"/><line x1="12" y1="1" x2="12" y2="4"/></svg>
    <span>February 22, 2019</span>
  </div>
  <p class="post-excerpt">We all want to get more done in the limited time we have. Procrastinations, distractions, and a host of other obstacles must be climbed and surmounted day by day in order to complete the tasks you set out to do. There are plenty of tools for productivity that we've covered before (like the Tempo Block Method)</p>
  <a class="btn-read" href="#">CONTINUE READING</a>
</article>

<section class="blog-section abs">
  <h2 class="section-title">OUR BLOG</h2>
  <div class="blog-grid">
    <article class="blog-card">
      <div class="card-image" role="img" aria-label="Row of colourful smartphones standing upright" style="background:linear-gradient(90deg,#2b3140 0%,#8a86a8 50%,#4a5f8a 100%)"></div>
      <div class="card-head">
        <div class="date-badge">29<small>FEB</small></div>
        <h3 class="card-title">Korvane Lumen Note 9 Review</h3>
      </div>
      <p class="card-text">More and more users are in to big phones with big beautiful high-resolution displays, such as Orbitel's Prism, PlusOne 6, or Pippin's Handset X.</p>
      <a class="btn-outline" href="#">READ MORE</a>
    </article>
    <article class="blog-card">
      <div class="card-image" role="img" aria-label="Close-up of a home electricity meter" style="background:linear-gradient(180deg,#9a9a98 0%,#c9c9c6 50%,#7d7d7a 100%)"></div>
      <div class="card-head">
        <div class="date-badge">29<small>FEB</small></div>
        <h3 class="card-title">How to Monitor Your Home Electricity Usage</h3>
      </div>
      <p class="card-text">Monitoring your electricity usage can help you keep track of how much you are spending on your energy. With this information</p>
      <a class="btn-outline" href="#">READ MORE</a>
    </article>
    <article class="blog-card">
      <div class="card-image" role="img" aria-label="Phone screen showing messaging app icons" style="background:linear-gradient(135deg,#2a3a3a 0%,#3f6b5a 50%,#2b5f8f 100%)"></div>
      <div class="card-head">
        <div class="date-badge">29<small>FEB</small></div>
        <h3 class="card-title">Is Your Messaging App Really Secure?</h3>
      </div>
      <p class="card-text">Messaging applications are one of the most—if not the most—important apps that we use every day.</p>
      <a class="btn-outline" href="#">READ MORE</a>
    </article>
  </div>
</section>

<section class="newsletter abs">
  <h2 class="section-title">SUBSCRIBE TO OUR NEWSLETTER</h2>
  <p class="newsletter-text">At vero eos et accusamus et iusto odio dignissimos ducimus qui blanditiis praesentium voluptatum deleniti atque corrupti</p>
  <form class="subscribe-form">
    <div class="subscribe-input">Enter Your E-mail Address</div>
    <div class="subscribe-btn">Subscribe</div>
  </form>
</section>

<footer class="site-footer abs">
  <a class="brand" href="#"><span class="brand-dot"></span>Quill Gadget Notes</a>
  <div class="social-row"><span></span><span></span><span></span><span></span></div>
  <nav class="footer-nav">
    <a href="#">Home</a><a href="#">Desktop</a><a href="#">Tips</a><a href="#">Software</a><a href="#">Other</a>
  </nav>
  <p class="copyright">Copyrights © 2019 All rights reserved</p>
</footer>

</body>
</html>
```